New Product Design

We want to develop new Wafer Biscuits Product design of Vanilla / strawberry / choclate flavour. Designer can design first any of the flavour ( Vanilla/Chcolate/Starwberry). Based on the first any variety design will go for other designs.
Wafer is in finger form .
Name of the Brand will be TOBI LUN
Wafer fingre (sample pics and TOBI LUN brand image is attached in word file for reference.

Smaple pics of the fingre is attached for ref.

Target Market(s)

Children and Youth

Industry/Entity Type

Food

```html
<!DOCTYPE html>
<html lang="en">
<head>
<meta charset="utf-8">
<title>TOBI LUN Wafer – Chocolate Flavour Wrapper</title>
<link rel="stylesheet" href="https://fonts.googleapis.com/css2?family=Montserrat:wght@500;800&family=Great+Vibes&display=swap">
<style>
  :root {
    --bg: #b8a47c;
    --wrapper: #0d0a09;
    --wrapper-edge: #1c1715;
    --seal: #151111;
    --gold: #c9a24e;
    --gold-light: #e6cf8c;
    --gold-dark: #8f6a2a;
    --cream: #f4f1ea;
    --white: #ffffff;
    --choco-deep: #2a120a;
    --choco: #4a2414;
    --choco-light: #7a4024;
    --wafer: #e8bf55;
    --wafer-light: #f3d98a;
  }
  * { margin: 0; padding: 0; box-sizing: border-box; }
  html, body {
    width: 1200px;
    height: 1100px;
    overflow: hidden;
    background: var(--bg);
  }
  .canvas {
    position: relative;
    width: 1200px;
    height: 1100px;
  }
  .wrapper-art {
    position: absolute;
    left: 0;
    top: 0;
  }
  .brand-name {
    font-family: "Montserrat", sans-serif;
    font-weight: 800;
    fill: var(--gold);
  }
  .badge-label {
    font-family: "Great Vibes", cursive;
    fill: var(--wrapper);
  }
  .flavour-script {
    font-family: "Great Vibes", cursive;
    fill: var(--gold);
  }
  .flavour-caption {
    font-family: "Montserrat", sans-serif;
    font-weight: 500;
    fill: var(--white);
    letter-spacing: 4px;
  }
</style>
</head>
<body>
<main class="canvas">
  <svg class="wrapper-art" width="1200" height="1100" viewBox="0 0 1200 1100" xmlns="http://www.w3.org/2000/svg">
    <defs>
      <linearGradient id="goldFill" x1="0" y1="0" x2="1" y2="1">
        <stop offset="0" stop-color="var(--gold-light)"/>
        <stop offset="0.5" stop-color="var(--gold)"/>
        <stop offset="1" stop-color="var(--gold-dark)"/>
      </linearGradient>
      <linearGradient id="bodyShade" x1="0" y1="0" x2="0" y2="1">
        <stop offset="0" stop-color="var(--wrapper-edge)"/>
        <stop offset="0.2" stop-color="var(--wrapper)"/>
        <stop offset="1" stop-color="var(--wrapper)"/>
      </linearGradient>
      <linearGradient id="productArt" x1="0" y1="1" x2="1" y2="0">
        <stop offset="0" stop-color="var(--choco-deep)"/>
        <stop offset="0.35" stop-color="var(--choco)"/>
        <stop offset="0.55" stop-color="var(--choco-light)"/>
        <stop offset="0.75" stop-color="var(--wafer)"/>
        <stop offset="1" stop-color="var(--wafer-light)"/>
      </linearGradient>
    </defs>

    <path class="seal seal-left" fill="var(--seal)"
      d="M170 330 L100 330 L120 352 L100 374 L120 396 L100 418 L120 440 L100 462 L120 484 L100 506 L120 528 L100 550 L120 572 L100 594 L120 616 L100 638 L120 660 L100 682 L120 704 L100 726 L120 748 L100 770 L170 770 Z"/>
    <path class="seal seal-right" fill="var(--seal)"
      d="M1030 330 L1100 330 L1080 352 L1100 374 L1080 396 L1100 418 L1080 440 L1100 462 L1080 484 L1100 506 L1080 528 L1100 550 L1080 572 L1100 594 L1080 616 L1100 638 L1080 660 L1100 682 L1080 704 L1100 726 L1080 748 L1100 770 L1030 770 Z"/>

    <rect class="wrapper-body" x="160" y="340" width="880" height="420" rx="14" fill="url(#bodyShade)"/>

    <rect class="product-illustration" role="img"
      aria-label="Illustration of a layered wafer finger dipped in a swirling chocolate splash with droplets"
      x="540" y="505" width="410" height="225" rx="18" fill="url(#productArt)"/>

    <g class="brand-seal">
      <ellipse cx="350" cy="520" rx="175" ry="150" fill="var(--cream)" stroke="url(#goldFill)" stroke-width="4"/>
      <text class="brand-name" x="350" y="505" text-anchor="middle" font-size="58">TOBI</text>
      <text class="brand-name" x="350" y="570" text-anchor="middle" font-size="58">LUN</text>
    </g>

    <g class="type-badge">
      <circle cx="440" cy="680" r="46" fill="url(#goldFill)"/>
      <text class="badge-label" x="440" y="689" text-anchor="middle" font-size="28">Wafer</text>
    </g>

    <g class="flavour-label">
      <text class="flavour-script" x="880" y="445" text-anchor="middle" font-size="60">Choclate</text>
      <text class="flavour-caption" x="880" y="484" text-anchor="middle" font-size="24">FLAVOUR</text>
    </g>
  </svg>
</main>
</body>
</html>
```